Business Card Revision

Need to redesign my business cards for a new professional look. We are a courier company. You can go to www.qvrunners.com to see what we do. The trucks have an old company name (Sprout) on them but that is the company we are just now
changing the name.

Target Market(s)

Potential clients. We service the automotive, plumbing, printing, air freight industries as well as many others.

Industry/Entity Type

Business

Contact Information for Business Card

QVmotion
20864 Lark Fenmore Parkway
Cincinnati, Oh 45873

Thomas R. Wendall
President

tom@qvrunners.com

Main: (513) 555-0147

```html
<!DOCTYPE html>
<html lang="en">
<head>
<meta charset="utf-8">
<title>QV Runners Stationery</title>
<link rel="stylesheet" href="https://fonts.googleapis.com/css2?family=Tinos:wght@400;700&display=swap">
<style>
  :root {
    --brand-blue: #1a72c4;
    --brand-green: #3db54a;
    --green-dark: #1f7a2c;
    --ink: #222;
    --paper: #ffffff;
    --backdrop: #eceef0;
    --edge: #3a4a55;
  }
  * { box-sizing: border-box; margin: 0; padding: 0; }
  html, body { width: 1200px; height: 747px; overflow: hidden; }
  body {
    background: var(--backdrop);
    font-family: "Tinos", "Times New Roman", serif;
    color: var(--ink);
    position: relative;
  }
  .brand-name {
    font-family: "Tinos", "Times New Roman", serif;
    font-weight: 700;
    color: var(--brand-blue);
    letter-spacing: 0.02em;
    line-height: 1;
    white-space: nowrap;
  }
  .hero-brand {
    position: absolute;
    left: 640px; top: 120px;
    width: 460px;
    text-align: center;
    font-size: 96px;
  }
  .sheet {
    position: absolute;
    background: var(--paper);
    box-shadow: 0 6px 18px rgba(0,0,0,0.18);
    overflow: hidden;
  }
  .sheet .wave { position: absolute; left: 0; bottom: 0; width: 100%; }

  /* Letterhead */
  .letterhead { left: 60px; top: 70px; width: 340px; height: 450px; }
  .letterhead .brand-name { position: absolute; left: 26px; top: 26px; font-size: 20px; }
  .letterhead .footer {
    position: absolute; right: 24px; bottom: 14px;
    text-align: right; font-size: 8px; line-height: 1.35; color: #111;
  }

  /* Envelope */
  .envelope { left: 430px; top: 420px; width: 400px; height: 220px; }
  .envelope .brand-name { position: absolute; left: 26px; top: 40px; font-size: 24px; }
  .envelope .stamp {
    position: absolute; right: 26px; top: 18px;
    width: 42px; height: 48px;
    border: 2px dashed #777;
  }

  /* Business card */
  .card { left: 860px; top: 450px; width: 300px; height: 172px; border-radius: 2px; }
  .card .backing { position: absolute; inset: 0; }
  .card .content {
    position: absolute; inset: 0;
    display: flex; flex-direction: column; align-items: center;
    padding-top: 14px; text-align: center;
  }
  .card .brand-name { font-size: 22px; margin-bottom: 8px; }
  .card .person { font-size: 14px; line-height: 1.1; }
  .card .role { font-size: 9px; color: var(--brand-blue); margin-bottom: 3px; }
  .card .contact { font-size: 9px; line-height: 1.25; }
  .card .address { font-size: 9px; line-height: 1.25; margin-top: 6px; }
</style>
</head>
<body>

  <div class="brand-name hero-brand">QV Runners</div>

  <section class="sheet letterhead">
    <div class="brand-name">QV Runners</div>
    <svg class="wave" width="340" height="100" viewBox="0 0 340 100" aria-hidden="true">
      <path d="M0 55 Q170 0 340 45 L340 100 L0 100 Z" fill="var(--brand-green)"/>
      <path d="M0 60 Q170 8 340 50 L340 62 Q170 22 0 72 Z" fill="var(--edge)" opacity="0.6"/>
      <path d="M0 40 Q170 -10 340 30 L340 52 Q170 12 0 62 Z" fill="var(--paper)"/>
    </svg>
    <div class="footer">
      (513) 555-0147<br>
      www.qvrunners.com<br>
      20864 Lark Fenmore Parkway<br>
      Cincinnati, Oh 45873
    </div>
  </section>

  <section class="sheet envelope">
    <div class="brand-name">QV Runners</div>
    <div class="stamp"></div>
    <svg class="wave" width="400" height="60" viewBox="0 0 400 60" aria-hidden="true">
      <path d="M0 38 Q200 0 400 32 L400 60 L0 60 Z" fill="var(--brand-green)"/>
      <path d="M0 30 Q200 -6 400 24 L400 34 Q200 4 0 42 Z" fill="var(--edge)" opacity="0.6"/>
    </svg>
  </section>

  <section class="sheet card">
    <svg class="backing" width="300" height="172" viewBox="0 0 300 172" aria-hidden="true">
      <defs>
        <linearGradient id="cardGreen" x1="0" y1="0" x2="1" y2="0">
          <stop offset="0" stop-color="var(--green-dark)"/>
          <stop offset="0.5" stop-color="var(--brand-green)"/>
          <stop offset="1" stop-color="var(--green-dark)"/>
        </linearGradient>
      </defs>
      <rect width="300" height="172" fill="url(#cardGreen)"/>
      <path d="M40 10 Q150 -2 260 10 Q286 86 260 162 Q150 174 40 162 Q14 86 40 10 Z" fill="var(--edge)" opacity="0.55" transform="translate(2 2)"/>
      <path d="M40 10 Q150 -2 260 10 Q286 86 260 162 Q150 174 40 162 Q14 86 40 10 Z" fill="var(--paper)"/>
    </svg>
    <div class="content">
      <div class="brand-name">QV Runners</div>
      <div class="person">Thomas R. Wendall</div>
      <div class="role">President</div>
      <div class="contact">(513) 555-0147<br>tom@qvrunners.com</div>
      <div class="address">20864 Lark Fenmore Parkway<br>Cincinnati, Oh 45873</div>
    </div>
  </section>

</body>
</html>
```